Travel Agency Website - Simple General

Need a 7 page simple design that is pretty repetitive. Need to be able to load quickly that is SEO optimized. Trying to give ideas on what they can do, be personal as we are local, but at the same time come across as professional and get information easily with little burden.

- Landing Page
- Marrowind Vacations Page
- Family Trips
- Road Trips from Texas
- Other Destinations
- About Us Page
- Contact Us Page

Target Market(s)

Families

Coding

Coded - Design and coding required

Number of Pages Required

5+ page

Colors

Designer to choose colors to be used in the design.

Requirements
Must have
• Like it to flow easily with our logo. Use that for colors, etc.

```html
<!DOCTYPE html>
<html lang="en">
<head>
<meta charset="utf-8">
<title>Hill Country Getaway – Texas Road Trips | Wander Lane Travel Co.</title>
<meta name="description" content="Hill Country Getaway: a 5 day Texas road trip for couples with van rental included.">
<link href="https://fonts.googleapis.com/css2?family=Outfit:wght@300;400;500;600;700;800&display=swap" rel="stylesheet">
<style>
:root{
  --teal:#1d5a66;
  --teal-dark:#174b55;
  --gold:#c4974a;
  --gold-light:#d8b06a;
  --ink:#2f3b3e;
  --muted:#4d5a5d;
  --line:#c9d0d2;
  --panel:#f4f3f0;
  --cream:#f1ece2;
  --white:#ffffff;
}
*{box-sizing:border-box;margin:0;padding:0}
html,body{width:1200px;height:2242px;overflow:hidden}
body{font-family:"Outfit",sans-serif;color:var(--ink);position:relative;
  background:linear-gradient(180deg,#f6f1e6 0,#efe8da 900px,#f3efe7 1600px,#e9ecea 2170px);}
.abs{position:absolute}

/* header */
.contact-bar{left:537px;top:0;width:558px;height:38px;background:var(--teal);border-radius:0 0 10px 10px;
  display:flex;align-items:center;gap:24px;padding-left:20px;color:#fff;font-size:13.5px;font-weight:500}
.contact-bar span{display:flex;align-items:center;gap:8px}
.contact-bar .ic{width:24px;height:24px;border-radius:50%;background:#fff;display:flex;align-items:center;justify-content:center}
.brand{left:78px;top:40px;display:flex;align-items:center;gap:10px;font-size:26px;font-weight:700;color:var(--teal)}
.brand .dot{width:22px;height:22px;border-radius:50%;background:var(--gold)}
.nav{left:306px;top:70px;display:flex;align-items:center;font-size:14.5px;font-weight:400;color:var(--teal)}
.nav a{color:inherit;text-decoration:none;position:absolute;top:0;white-space:nowrap}
.nav .active::after{content:"";position:absolute;left:0;right:0;bottom:-9px;height:2px;background:var(--gold)}
.btn{background:var(--gold);color:#fff;border-radius:30px;display:flex;align-items:center;justify-content:space-between;font-weight:600}
.btn .arrow{border-radius:50%;background:var(--gold-light);display:flex;align-items:center;justify-content:center}
.contact-btn{left:953px;top:62px;width:137px;height:36px;font-size:13px;font-weight:500;padding:0 6px 0 25px}
.contact-btn .arrow{width:26px;height:26px}

/* hero */
.hero-photo{left:0;top:0;width:1200px;height:560px;
  background:linear-gradient(100deg,rgba(246,241,230,1) 0%,rgba(246,241,230,.95) 32%,rgba(214,190,130,.75) 52%,#9c8a48 64%,#6f7634 78%,#8b6f3a 100%);
  -webkit-mask:linear-gradient(180deg,#000 80%,transparent);mask:linear-gradient(180deg,#000 80%,transparent)}
.hero-eyebrow{left:130px;top:222px;font-size:20px;font-weight:400;color:var(--teal);letter-spacing:.3px}
.hero-title{left:128px;top:250px;font-size:50px;line-height:54px;font-weight:700;color:var(--teal);letter-spacing:.5px}
.hero-copy{left:130px;top:371px;width:360px;font-size:13.5px;line-height:19.5px;color:var(--ink)}

/* trip card */
.trip-card{left:104px;top:536px;width:988px;height:943px;background:#fff;border-radius:12px}
.h2{font-size:28px;font-weight:700;color:var(--teal);letter-spacing:.3px}
.about-title{left:183px;top:596px}
.about-copy{left:183px;top:650px;width:560px;font-size:13.3px;line-height:16.5px;color:var(--muted)}
.about-copy p+p{margin-top:18px}
.itin-title{left:185px;top:803px;font-size:23px}
.day{left:181px;display:flex;gap:22px;width:540px}
.day .photo{width:124px;height:83px;border-radius:6px;flex:none}
.day .label{font-size:13.5px;font-weight:600;color:var(--gold);margin-top:4px}
.day h3{font-size:13px;font-weight:600;color:var(--ink);margin-top:6px}
.day p{font-size:13px;line-height:18.5px;color:var(--muted);margin-top:4px}

.price-panel{left:787px;top:595px;width:263px;height:598px;background:var(--panel);border-radius:4px;overflow:hidden}
.price-head{height:152px;background:var(--teal);color:#fff;text-align:center;padding-top:34px}
.price-head .k{font-size:17px;font-weight:600;letter-spacing:.3px}
.price-head .v{font-size:38px;font-weight:700;line-height:44px}
.price-head .u{font-size:15px}
.stat{position:absolute;left:28px;width:218px;height:74px;display:flex;align-items:center;gap:18px;padding-left:8px}
.stat+.stat{border-top:1px solid var(--line)}
.stat .t{font-size:15px;line-height:22px;color:var(--ink)}
.stat .t b{font-weight:600}
.plan-btn{position:absolute;left:21px;top:505px;width:221px;height:45px;font-size:18px;padding:0 8px 0 51px}
.plan-btn .arrow{width:32px;height:32px}

/* form */
.plan-form{left:104px;top:1508px;width:1000px;height:604px;border:1px solid #d9ddd8;border-radius:6px;
  background:linear-gradient(180deg,#fff 0%,#fbfbf9 60%,#eaefed 100%)}
.form-title{left:0;top:1553px;width:1190px;text-align:center;font-size:31px}
.spark{left:813px;top:1543px}
.lbl{font-size:16.5px;font-weight:500;color:var(--teal)}
.field{border:1px solid #9aaeb3;border-radius:2px;background:#fff;display:flex;align-items:center;font-size:16px;color:var(--muted);padding:0 24px}
.field.sel{justify-content:space-between}
.field.date{gap:14px;padding-left:18px}
.submit-btn{left:482px;top:2014px;width:251px;height:51px;font-size:20px;padding:0 8px 0 58px}
.submit-btn .arrow{width:36px;height:36px}

/* footer */
.footer{left:0;top:2170px;width:1200px;height:72px;background:#fff}
.footer p{position:absolute;left:0;width:1170px;top:21px;text-align:center;font-size:13px;color:var(--ink)}
.social{position:absolute;top:17px;width:22px;height:22px;border-radius:50%;background:var(--teal)}
</style>
</head>
<body>

<div class="abs hero-photo" role="img" aria-label="Sunlit limestone cliffs above a winding hill country road"></div>

<header>
  <div class="abs contact-bar">
    <span><i class="ic"><svg width="13" height="10" viewBox="0 0 13 10"><rect x=".5" y=".5" width="12" height="9" rx="1" fill="none" stroke="#1d5a66"/><path d="M1 1l5.5 4.5L12 1" fill="none" stroke="#1d5a66"/></svg></i>hello@wanderlanetravel.example</span>
    <span><i class="ic"><svg width="12" height="12" viewBox="0 0 24 24"><path fill="#1d5a66" d="M6.6 10.8a15 15 0 006.6 6.6l2.2-2.2c.3-.3.7-.4 1-.2 1.1.4 2.3.6 3.6.6.6 0 1 .4 1 1V20c0 .6-.4 1-1 1A17 17 0 013 4c0-.6.4-1 1-1h3.5c.6 0 1 .4 1 1 0 1.3.2 2.5.6 3.6.1.3 0 .7-.2 1z"/></svg></i>Phone Number (555) 014 2290</span>
  </div>
  <div class="abs brand"><i class="dot"></i>Wander Lane</div>
  <nav class="abs nav">
    <a style="left:2px;top:3px" aria-label="Home"><svg width="14" height="13" viewBox="0 0 14 13"><path d="M7 0l7 6h-2v7H9V9H5v4H2V6H0z" fill="#c4974a"/></svg></a>
    <a style="left:37px">Marrowind Vacations</a>
    <a style="left:173px">Family Trips</a>
    <a style="left:274px" class="active">Texas Road Trips</a>
    <a style="left:407px">Other Destinations</a>
    <a style="left:569px">About Us</a>
  </nav>
  <a class="abs btn contact-btn">Contact Us <i class="arrow"><svg width="10" height="10" viewBox="0 0 10 10"><path d="M2 8L8 2M3.5 2H8v4.5" stroke="#fff" stroke-width="1.5" fill="none"/></svg></i></a>
</header>

<section>
  <p class="abs hero-eyebrow">TEXAS ROAD TRIPS</p>
  <h1 class="abs hero-title">HILL COUNTRY<br>GETAWAY</h1>
  <p class="abs hero-copy">Scenic routes. Unforgettable places. Epic adventures. Explore handpicked road trips perfect for families, couples, and adventure seekers.</p>
</section>

<main>
  <div class="abs trip-card"></div>
  <h2 class="abs h2 about-title">ABOUT THE TRIP</h2>
  <div class="abs about-copy">
    <p>Lorem ipsum dolor sit amet, consectetur adipiscing elit, sed do eiusmod tempor incididunt ut labore et dolore magna aliqua. Quis ipsum suspendisse ultrices gravida.</p>
    <p>Lorem ipsum dolor sit amet, consectetur adipiscing elit, sed do eiusmod tempor incididunt ut labore et dolore magna aliqua. Quis ipsum suspendisse ultrices gravida. Risus commodo viverra maecenas accumsan lacus vel facilisis.</p>
  </div>

  <h2 class="abs h2 itin-title">ITINERARY OVERVIEW</h2>
  <article class="abs day" style="top:853px"><div class="photo" role="img" aria-label="Highway at sunset with water tower" style="background:linear-gradient(180deg,#e98a5a,#f2b07a 45%,#3d3a33 70%,#2b2d2c)"></div><div><p class="label">Day 1</p><h3>Lorem ipsum dolor sit amet consectetur</h3><p>adipiscing elit, sed do eiusmod tempor incididunt ut labore et dolore magna aliqua. Quis ipsum suspendisse ultrices</p></div></article>
  <article class="abs day" style="top:966px;gap:20px"><div class="photo" role="img" aria-label="Road through a desert canyon" style="background:linear-gradient(180deg,#9fb7c9,#a07a5a 35%,#7d8a4a 65%,#3a3634)"></div><div><p class="label">Day 2</p><h3>Lorem ipsum dolor sit amet consectetur</h3><p>adipiscing elit, sed do eiusmod tempor incididunt ut labore et dolore magna aliqua. Quis ipsum suspendisse ultrices</p></div></article>
  <article class="abs day" style="top:1084px;gap:21px"><div class="photo" role="img" aria-label="Mountain road under a blue sky" style="background:linear-gradient(180deg,#2aa6d6,#7ac6e0 30%,#8a6a4c 55%,#3a3634)"></div><div><p class="label">Day 3</p><h3>Lorem ipsum dolor sit amet consectetur</h3><p>adipiscing elit, sed do eiusmod tempor incididunt ut labore et dolore magna aliqua. Quis ipsum suspendisse ultrices</p></div></article>
  <article class="abs day" style="top:1198px;gap:19px"><div class="photo" role="img" aria-label="Canyon overlook at dusk" style="background:linear-gradient(180deg,#c7b8c6,#e2b89a 30%,#a45a3a 55%,#5c4a3a)"></div><div><p class="label">Day 4</p><h3>Lorem ipsum dolor sit amet consectetur</h3><p>adipiscing elit, sed do eiusmod tempor incididunt ut labore et dolore magna aliqua. Quis ipsum suspendisse ultrices</p></div></article>
  <article class="abs day" style="top:1318px;gap:21px"><div class="photo" role="img" aria-label="Desert highway beside a golden mesa" style="background:linear-gradient(180deg,#2f6fb0,#e3a04a 40%,#c8792f 65%,#5b5148)"></div><div><p class="label">Day 4</p><h3>Lorem ipsum dolor sit amet consectetur</h3><p>adipiscing elit, sed do eiusmod tempor incididunt ut labore et dolore magna aliqua. Quis ipsum suspendisse ultrices</p></div></article>

  <aside class="abs price-panel">
    <div class="price-head"><p class="k">TRIP PRICE</p><p class="v">$250</p><p class="u">Per Person</p></div>
    <div class="stat" style="top:184px"><svg width="34" height="34" viewBox="0 0 34 34" fill="none" stroke="#c4974a" stroke-width="1.6"><circle cx="17" cy="17" r="7"/><path d="M17 2v5M17 27v5M2 17h5M27 17h5M6.4 6.4l3.5 3.5M24.1 24.1l3.5 3.5M6.4 27.6l3.5-3.5M24.1 9.9l3.5-3.5"/></svg><p class="t">Duration<br><b>5 Days/ 4 Nights</b></p></div>
    <div class="stat" style="top:258px"><svg width="34" height="34" viewBox="0 0 34 34" fill="none" stroke="#c4974a" stroke-width="1.6"><circle cx="11" cy="13" r="4"/><circle cx="23" cy="13" r="4"/><path d="M3 30c0-5 4-9 8-9s8 4 8 9M15 30c0-5 4-9 8-9s8 4 8 9M3 30h28"/><path d="M17 6l-2-2a1.5 1.5 0 012 -1 1.5 1.5 0 012 1z"/></svg><p class="t">Best for<br><b>Couples</b></p></div>
    <div class="stat" style="top:332px"><svg width="38" height="30" viewBox="0 0 38 30"><path d="M1 26L13 8l5 7 5-9 14 20z" fill="#c4974a"/><path d="M11 11l2-3 3 4z" fill="#fff"/></svg><p class="t">Destination<br><b>Hill Country</b></p></div>
    <div class="stat" style="top:406px"><svg width="38" height="28" viewBox="0 0 38 28" fill="none" stroke="#c4974a" stroke-width="1.6"><path d="M2 21V8c0-2 1-3 3-3h21l8 8 2 2v6H2z"/><path d="M7 10h7v4H7zM18 10h6l4 4H18z"/><circle cx="9" cy="22" r="3" fill="#f4f3f0"/><circle cx="29" cy="22" r="3" fill="#f4f3f0"/></svg><p class="t">Van Rental<br><b>Included</b></p></div>
    <a class="btn plan-btn">Start Planning <i class="arrow"><svg width="12" height="12" viewBox="0 0 10 10"><path d="M2 8L8 2M3.5 2H8v4.5" stroke="#fff" stroke-width="1.5" fill="none"/></svg></i></a>
  </aside>
</main>

<section>
  <div class="abs plan-form"></div>
  <h2 class="abs h2 form-title">PLAN YOUR TEXAS ROAD TRIP</h2>
  <svg class="abs spark" width="16" height="16" viewBox="0 0 16 16"><path d="M8 0C8.6 6 10 7.4 16 8 10 8.6 8.6 10 8 16 7.4 10 6 8.6 0 8 6 7.4 7.4 6 8 0z" fill="#c4974a"/></svg>

  <label class="abs lbl" style="left:161px;top:1629px">What Type of Trip Are You Interested In?</label>
  <label class="abs lbl" style="left:620px;top:1629px">How Many People in Your Party?</label>
  <div class="abs field sel" style="left:161px;top:1666px;width:442px;height:56px">Select <svg width="16" height="10" viewBox="0 0 16 10"><path d="M1 1l7 7 7-7" stroke="#1d5a66" stroke-width="2" fill="none"/></svg></div>
  <div class="abs field sel" style="left:618px;top:1665px;width:215px;height:56px;padding:0 14px 0 22px">No. of Adults <svg width="16" height="10" viewBox="0 0 16 10" style="margin-top:8px"><path d="M1 1l7 7 7-7" stroke="#1d5a66" stroke-width="2" fill="none"/></svg></div>
  <div class="abs field sel" style="left:842px;top:1665px;width:215px;height:56px;padding:0 14px 0 22px">No. of Kids <svg width="16" height="10" viewBox="0 0 16 10"><path d="M1 1l7 7 7-7" stroke="#1d5a66" stroke-width="2" fill="none"/></svg></div>

  <label class="abs lbl" style="left:161px;top:1746px">Do you need a Van Rental?</label>
  <label class="abs lbl" style="left:624px;top:1746px">When Would You Like To Go?</label>
  <div class="abs field sel" style="left:161px;top:1781px;width:442px;height:56px">Yes <svg width="16" height="10" viewBox="0 0 16 10"><path d="M1 1l7 7 7-7" stroke="#1d5a66" stroke-width="2" fill="none"/></svg></div>
  <div class="abs field date" style="left:620px;top:1781px;width:215px;height:56px"><svg width="19" height="20" viewBox="0 0 19 20" fill="none" stroke="#b8bec0" stroke-width="1.5"><rect x="1" y="3" width="17" height="16" rx="2"/><path d="M1 8h17M5 1v4M14 1v4"/><path d="M5 11h2M9 11h2M13 11h1M5 15h2M9 15h2" /></svg>Start Date</div>
  <div class="abs field date" style="left:844px;top:1781px;width:215px;height:56px"><svg width="19" height="20" viewBox="0 0 19 20" fill="none" stroke="#b8bec0" stroke-width="1.5"><rect x="1" y="3" width="17" height="16" rx="2"/><path d="M1 8h17M5 1v4M14 1v4"/><path d="M5 11h2M9 11h2M13 11h1M5 15h2M9 15h2" /></svg>End Date</div>

  <label class="abs lbl" style="left:161px;top:1850px">Any Additional Notes</label>
  <div class="abs field" style="left:161px;top:1884px;width:898px;height:110px;align-items:flex-start;padding:22px 27px">Type here</div>

  <a class="abs btn submit-btn">Start Planning <i class="arrow"><svg width="13" height="13" viewBox="0 0 10 10"><path d="M2 8L8 2M3.5 2H8v4.5" stroke="#fff" stroke-width="1.5" fill="none"/></svg></i></a>
</section>

<footer class="abs footer">
  <p>© 2026 Wander Lane Travel Co. All Right Reserved</p>
  <i class="social" style="left:994px" aria-label="Social link"></i>
  <i class="social" style="left:1024px" aria-label="Social link"></i>
</footer>

</body>
</html>
```